Psychology service brochure

Marketing brochure for a new psychological counselling service.
Our old brochure was too boring and conservative. We are selling our services to GP's, psychiatrists, other health providers and of course potential clients. We'd really like a professional, elegant look that conveys us to be compassionate and conscientious providers of psychological services.
I have included a copy of our old brochure and a copy of the changes we'd like to the text.
Updates
I have included a photo of myself and my business partner. Only the faces are needed, so backgrounds would need to be edited out.
Hello, in consultation with my business partner, we would like
the use of our photos in the brochure please (with backgrounds edited out)
no stock photos of random people
use of abstract or nature/floral motifs suggestive of tranquillity
regards,
Miriam
Target Market(s)
General practitioner doctors, potential clients
Industry/Entity Type
Health
Requirements
Must have
- must include BlairMdITC TT- font for the business name
- must include our signature color Pantone 291 (see attached brochure)
- use of the photos of myself and my business partner (with background edited out please)
- keep use of colours to a minimum, 3 colors maximum, one of which must be Pantone 291
- must include changes to the brochure as outlined in the 'Changes to Pamphlet' document.
Nice to have
- an interesting, eye catching layout.
- interesting use of white spaces
- use of subtle abstract or nature/floral related graphics suggestive of tranquillity
Should not have
- should not include our fee
- stock photos of people

```html
<!DOCTYPE html>
<html lang="en">
<head>
<meta charset="utf-8">
<title>Psychology Practice Brochure – Inside Spread</title>
<link rel="stylesheet" href="https://fonts.googleapis.com/css2?family=Marcellus+SC&family=Roboto+Condensed:wght@400&family=Arimo:wght@400;700&display=swap">
<style>
  :root{
    --sky:#a3cdea;
    --sky-pale:#c9e2f4;
    --blue:#4fa3d8;
    --ink:#1c1c1c;
    --paper:#ffffff;
    --skin-light:#f3e6d8;
    --skin-mid:#e9cdb4;
  }
  html,body{margin:0;padding:0;overflow:hidden;}
  body{width:1200px;height:806px;background:var(--paper);}
  .spread{position:relative;width:1200px;height:806px;overflow:hidden;background:var(--paper);color:var(--ink);}
  .top-band{position:absolute;left:0;top:0;width:1200px;height:44px;background:var(--sky);}
  .top-edge{position:absolute;left:0;top:44px;width:1200px;height:8px;background:var(--sky-pale);}
  .bottom-band{position:absolute;left:0;top:662px;width:1200px;height:144px;background:var(--sky);}
  .bottom-stripe{position:absolute;left:0;top:669px;width:1200px;height:21px;background:var(--sky-pale);}
  .flourish{position:absolute;top:738px;width:96px;height:34px;border-radius:17px;background:rgba(255,255,255,.35);}
  .flourish--left{left:130px;}
  .flourish--mid{left:537px;}
  .portrait{position:absolute;border-radius:0 0 10px 10px;}
  .portrait--miriam{left:252px;top:52px;width:150px;height:415px;
    background:linear-gradient(180deg,var(--skin-light) 0%,var(--skin-mid) 45%,rgba(255,255,255,0) 100%);}
  .portrait--jessica{left:633px;top:52px;width:152px;height:400px;
    background:linear-gradient(180deg,var(--skin-light) 0%,var(--skin-mid) 50%,rgba(255,255,255,0) 100%);}
  .profile{position:absolute;top:70px;font-family:"Roboto Condensed",sans-serif;font-size:14px;line-height:17.2px;}
  .profile--miriam{left:61px;}
  .profile--jessica{left:448px;}
  .profile h2,.fees h2{font-family:"Marcellus SC",serif;font-weight:400;font-size:16.5px;line-height:17px;margin:0 0 14px;letter-spacing:2.2px;}
  .profile p{margin:0 0 17.2px;}
  .fees{position:absolute;left:827px;top:62px;width:340px;font-family:Arimo,sans-serif;font-size:12px;line-height:17.5px;}
  .fees h2{margin-bottom:18px;}
  .fees p{margin:0 0 17.5px;}
  .fees .notice{font-weight:700;margin-top:35px;}
  .bubbles{position:absolute;left:0;top:0;}
</style>
</head>
<body>
<main class="spread">
  <div class="top-band"></div>
  <div class="top-edge"></div>
  <div class="bottom-band"></div>
  <div class="bottom-stripe"></div>
  <div class="flourish flourish--left" role="img" aria-label="White floral flourish ornament"></div>
  <div class="flourish flourish--mid" role="img" aria-label="White floral flourish ornament"></div>

  <div class="portrait portrait--miriam" role="img" aria-label="Portrait photo of Miriam Hale, fading into white"></div>
  <div class="portrait portrait--jessica" role="img" aria-label="Portrait photo of Jessica Marlow, fading into white"></div>

  <section class="profile profile--miriam">
    <h2>Miriam Hale<br>Clinical Psychologist<br>M.Psych (Clin.) MAPS</h2>
    <p>Miriam is a Clinical Psychologist<br>with  fifteen years of experience<br>providing a range of psychological<br>services to challenging  clients<br>within the public mental health<br>sector including forensic, addiction<br>and dual  diagnosis services.<br>She has been employed as a Senior<br>Psychologist in this capacity for<br>the last seven years.</p>
    <p>Miriam is a trained and experienced<br>Cognitive Behavioural Therapist and is<br>skilled in treating individuals and<br>groups with a range of mood disorders<br>including anxiety, depression and panic<br>disorder, as well as in helping clients<br>to overcome life issues such as grief<br>and loss, stress management and anger<br>management.</p>
    <p>Miriam trains other mental health cli-<br>nicians and university students in treatment<br>modalities including Motivational<br>Interviewing and Brief Interventions.<br>She has an interest in brain-based<br>research into neuroplasticity and<br>it is application to cognitive therapy and<br>change.</p>
  </section>

  <section class="profile profile--jessica">
    <h2>Jessica Marlow<br>Clinical Psychologist<br>M.Psych (Clin.) MAPS</h2>
    <p>Jessica is a Clinical Psychologist,<br>and with fifteen years experience working<br>in the public health sector, seven as<br>a Senior Psychologist, she is a highly<br>skilled clinician in the areas of<br>mental health, addiction and dual<br>diagnosis.</p>
    <p>She has more recently specialised<br>in working with adolescents but has<br>significant experience treating adults,<br>both individually and in a variety of group<br>programmes. She has also facilitated<br>numerous training events and mentored<br>clinicians in addressing dual diagnosis<br>issues with their clients.</p>
    <p>Jessica primarily utilises a cognitive<br>behavioural framework, motivational<br>inter-viewing, and has a special interest<br>in working with adolescents who are<br>experiencing develop-mental difficulties,<br>antenatal and post-natal depression/stress,<br>and parenting issues.<br>Additionally Jessica is skilful working in<br>the areas of grief &amp; loss, life transition and<br>adjustment issues, relationship and<br>interpersonal challenges, and personal<br>development.</p>
  </section>

  <section class="fees">
    <h2>Our Fee Structure</h2>
    <p>The practice accepts referrals from self-referring<br>individuals, as well as from health professionals<br>such as GPs, Psychiatrists, and Maternal and<br>Child Health Nurses.</p>
    <p>Medicare rebates are available for clients referred<br>for treatment by their GP. There are different tiers of<br>rebates for Psychologists under Medicare, and this is<br>dependent on treatment received (individual, group<br>or pregnancy support counselling), and whether<br>you are treated by a Psychologist or a Clinical<br>Psychologist.</p>
    <p>Please contact us directly to further discuss fees for<br>treatment. Fees are paid in full at the end of<br>each session, and a receipt is provided which will<br>allow you to obtain your refund at any Medicare office.</p>
    <p class="notice">The practice does not bulk bill at this time, but<br>we anticipate the addition of this facility<br>in the future.</p>
  </section>

  <svg class="bubbles" width="1200" height="806" viewBox="0 0 1200 806" aria-hidden="true">
    <circle cx="776" cy="682" r="80" fill="#ffffff"/>
    <circle cx="776" cy="682" r="67" fill="#4fa3d8"/>
    <circle cx="905" cy="751" r="61" fill="#ffffff"/>
    <circle cx="905" cy="751" r="47" fill="#4fa3d8"/>
    <circle cx="973" cy="703" r="26" fill="#ffffff"/>
    <circle cx="973" cy="703" r="19" fill="#4fa3d8"/>
  </svg>
</main>
</body>
</html>
```